Facebook Ad For New online Spectacle Store

We have started a new online store in Australia selling spectacles. As we don't have overheads such as rent electricity etc we are able to do these glasses at an extremely cheap price of $50 for the complete pair. We want to highlight the affordability and quality. This ad will be promoted on Facebook all over Australia. We want to make an impression. There are a lot of people wearing cheap magnifiers from chemists etc that are not suitable as most people need a corrective lens and rarely are both eyes the same power. So it's the people that are buying the $10 glasses we really want to sway to get ones that actually are the correct prescription for them without paying hundreds of dollars on a pair. "Throw away your magnifiers" As it's Facebook we can't really have too much writing in the image HOWEVER we want to highlight COMPLETE GLASSES $50 and that they will be the customers exact power lens. Our Website is www.lumaframes.com.au I have uploaded our logo but you do not need it in the design. We will be adding text to the Ad but not in the image you design (except for complete glasses for $50). you can take some of the images of frames from the website or I can upload just ask- tell me which one suits your design. Basically you have freedom to come up with something that will impress our potential customers make them click the link and check out our website.

Target Market(s)

People that use Cheap magnifiers - our glasses are a upgrade and better for their eyes

Industry/Entity Type

Eyewear

Colors

Designer to choose colors to be used in the design.

Requirements
Must have
• Complete Glasses $50 (Plus postage)- The (plus postage) in smaller writing than the Complete glasses for $50 part

```html
<!DOCTYPE html>
<html lang="en">
<head>
<meta charset="utf-8">
<title>Complete Glasses $50 – Luma Frames</title>
<link rel="stylesheet" href="https://fonts.googleapis.com/css2?family=Playfair+Display:ital,wght@1,700;1,800;1,900&display=swap">
<style>
  :root {
    --paper: #ffffff;
    --ink: #3b3b3d;
    --accent: #22b4e4;
    --frame-navy: #2c3560;
    --frame-navy-soft: #6f7896;
    --frame-gold: #c9bfa8;
    --frame-gold-soft: #eeeae2;
  }
  * { margin: 0; padding: 0; box-sizing: border-box; }
  html, body {
    width: 1200px;
    height: 444px;
    overflow: hidden;
    background: var(--paper);
  }
  .ad {
    position: relative;
    width: 1200px;
    height: 444px;
    background: var(--paper);
    font-family: "Playfair Display", "Bodoni Moda", Georgia, serif;
    font-style: italic;
    color: var(--ink);
  }
  .headline-band {
    position: absolute;
    left: 0;
    top: 92px;
    width: 630px;
    height: 98px;
    background: linear-gradient(90deg, var(--accent) 0%, #8fd6f0 35%, rgba(255,255,255,0) 100%);
  }
  .headline {
    position: absolute;
    left: 20px;
    top: 106px;
    font-size: 57px;
    font-weight: 800;
    letter-spacing: 1px;
    line-height: 1;
    text-transform: uppercase;
    white-space: nowrap;
    color: var(--ink);
  }
  .price {
    position: absolute;
    left: 196px;
    top: 205px;
    font-size: 142px;
    font-weight: 800;
    line-height: 1;
    letter-spacing: -2px;
    color: var(--ink);
    text-shadow: -5px 0 0 var(--accent);
  }
  .postage-note {
    position: absolute;
    left: 14px;
    top: 418px;
    font-size: 11px;
    font-weight: 800;
    letter-spacing: 0.3px;
    text-transform: uppercase;
    color: #1e1e1e;
  }
  .frame-photo {
    position: absolute;
    border-radius: 40px;
  }
  .frame-photo--round {
    left: 700px;
    top: 38px;
    width: 444px;
    height: 160px;
    background: radial-gradient(ellipse at center, var(--frame-navy-soft) 0%, var(--frame-navy) 60%, rgba(44,53,96,0.15) 100%);
  }
  .frame-photo--aviator {
    left: 714px;
    top: 234px;
    width: 430px;
    height: 176px;
    background: radial-gradient(ellipse at center, var(--frame-gold-soft) 0%, var(--frame-gold) 65%, rgba(201,191,168,0.2) 100%);
  }
</style>
</head>
<body>
  <main class="ad">
    <div class="headline-band"></div>
    <h1 class="headline">Complete Glasses</h1>
    <p class="price">$50</p>
    <p class="postage-note">*Plus postage</p>
    <div class="frame-photo frame-photo--round" role="img" aria-label="Photo of round navy tortoiseshell spectacle frames"></div>
    <div class="frame-photo frame-photo--aviator" role="img" aria-label="Photo of gold stainless steel double-bridge spectacle frames"></div>
  </main>
</body>
</html>
```